Sweet corn and halves apricot label design!

We are planning to launch two new products, Halves Apricot and Sweet Corn, which are part of the same family of products as the Peach Halves. Each product will have its own unique packaging design, with Halves Apricot featuring green lids, similar to the Peach Halves packaging.
Given your exceptional work on the Peach Halves design, we believe that your creative vision and expertise would be a perfect fit for these new projects. We invite you to bring your unique perspective to the table and help us create packaging designs that will captivate our customers and complement our existing product line. (HALVES PEACHES)
Product name : SWEET CORN / MAÏS DOUX
Ingredients : CORN, WATER, SALT. / Maïs, eau, sel.
Weight : 210g
Barcode : leave it a space
QR Code : leave it space
Product name : Apricot halves in light syrup / Abricot en moitiés dans un syrop léger
Ingredients : Apricot, water, sugar
Weight : 220g:

```html
<!DOCTYPE html>
<html lang="en">
<head>
<meta charset="utf-8">
<title>Sweet Corn – Maïs Doux Label</title>
<link rel="stylesheet" href="https://fonts.googleapis.com/css2?family=Montserrat:wght@700;800&family=PT+Serif:wght@400;700&display=swap">
<style>
  :root {
    --backdrop: #f1f1f1;
    --corn-light: #f7c93a;
    --corn-deep: #eeab1f;
    --leaf-green: #22ab5c;
    --leaf-green-dark: #127c38;
    --wheat-gold: #d9ca80;
    --label-white: #ffffff;
    --ink: #1b1b1b;
    --sketch-light: #fbe07a;
    --sketch-deep: #e9b42a;
  }
  html, body {
    margin: 0;
    padding: 0;
    width: 1200px;
    height: 1200px;
    overflow: hidden;
    background: var(--backdrop);
  }
  .label-stage {
    width: 1200px;
    height: 1200px;
    display: flex;
    align-items: center;
    justify-content: center;
  }
  .product-label {
    width: 1045px;
    height: 750px;
    display: block;
  }
  .brand-name {
    font-family: "Montserrat", sans-serif;
    font-weight: 800;
    font-size: 46px;
    letter-spacing: 2px;
    fill: var(--label-white);
  }
  .product-title {
    font-family: "Montserrat", sans-serif;
    font-weight: 700;
    font-size: 96px;
    letter-spacing: 1px;
  }
  .product-title--en { fill: var(--label-white); }
  .product-title--fr { fill: var(--wheat-gold); }
  .net-weight {
    font-family: "PT Serif", serif;
    font-weight: 700;
    font-size: 19px;
    fill: var(--ink);
  }
  .claim-text {
    font-family: "PT Serif", serif;
    font-weight: 400;
    font-size: 17px;
    fill: var(--label-white);
  }
</style>
</head>
<body>
<main class="label-stage">
  <svg class="product-label" viewBox="0 0 1045 750" xmlns="http://www.w3.org/2000/svg" aria-label="Sweet corn jar label">
    <defs>
      <linearGradient id="cornBase" x1="0" y1="0" x2="0" y2="1">
        <stop offset="0" stop-color="var(--corn-light)"/>
        <stop offset="1" stop-color="var(--corn-deep)"/>
      </linearGradient>
      <linearGradient id="greenBand" x1="0" y1="0" x2="1" y2="0">
        <stop offset="0" stop-color="var(--leaf-green)"/>
        <stop offset="1" stop-color="var(--leaf-green-dark)"/>
      </linearGradient>
      <linearGradient id="cobSketch" x1="0" y1="1" x2="1" y2="0">
        <stop offset="0" stop-color="var(--sketch-light)"/>
        <stop offset="1" stop-color="var(--sketch-deep)"/>
      </linearGradient>
    </defs>

    <rect class="label-base" x="0" y="0" width="1045" height="750" fill="url(#cornBase)"/>

    <rect class="corn-illustration" x="60" y="465" width="720" height="285" rx="20"
          fill="url(#cobSketch)" opacity="0.75"
          role="img" aria-label="Engraved illustration of a sweet corn cob with husk leaves"/>

    <rect class="title-band" x="0" y="130" width="900" height="330" fill="url(#greenBand)"/>

    <polygon class="side-panel" points="885,0 1045,0 1045,750 775,750" fill="url(#greenBand)"/>

    <text class="brand-name" x="505" y="175" text-anchor="middle">SOLVANE</text>

    <text class="product-title product-title--en" x="505" y="322" text-anchor="middle">SWEET CORN</text>
    <text class="product-title product-title--fr" x="505" y="428" text-anchor="middle">MAÏS DOUX</text>

    <text class="net-weight" x="622" y="722">Net Wt.210g</text>

    <g class="natural-badge">
      <circle cx="885" cy="600" r="46" fill="none" stroke="var(--label-white)" stroke-width="2"/>
      <circle cx="885" cy="600" r="30" fill="none" stroke="var(--label-white)" stroke-width="1.5"/>
    </g>
    <text class="claim-text" x="885" y="675" text-anchor="middle">NO ADDED</text>
    <text class="claim-text" x="885" y="699" text-anchor="middle">PRESERVATIVES</text>
  </svg>
</main>
</body>
</html>
```